A Book Cover For a Book Called "Tamsire"

Attached are two files for the ISBN bar graph for the print version of the cover! Same image, just two different formats.
Updates

Project Deadline Extended Reason: We'd like to see a few more designs, and work with a few of the designs already submitted. Added Tuesday, October 24, 2017

Target Market(s)

young adult female, parents

Colors

Designer to choose colors to be used in the design.

```html
<!DOCTYPE html>
<html lang="en">
<head>
<meta charset="utf-8">
<title>Tamsire – A Memoir</title>
<link rel="stylesheet" href="https://fonts.googleapis.com/css2?family=Comfortaa:wght@300&family=Cinzel:wght@400&family=Great+Vibes&display=swap">
<style>
  :root {
    --page: #ffffff;
    --ink-dark: #050205;
    --plum: #8a2a78;
    --plum-deep: #6b1f5e;
    --glow: #ffffff;
    --glow-halo: rgba(230, 170, 255, 0.85);
    --ghost: rgba(20, 20, 20, 0.55);
  }
  * { margin: 0; padding: 0; box-sizing: border-box; }
  html, body {
    width: 960px;
    height: 1200px;
    overflow: hidden;
    background: var(--page);
  }
  .canvas {
    position: relative;
    width: 960px;
    height: 1200px;
    background: var(--page);
  }
  .guide-line {
    position: absolute;
    left: 0;
    top: 52px;
    width: 470px;
    height: 2px;
    background: #555;
  }
  .cover {
    position: absolute;
    left: 42px;
    top: 18px;
    width: 882px;
    height: 1182px;
    background: var(--ink-dark);
    overflow: hidden;
    box-shadow: 4px 0 0 #9a9a9a;
  }
  .cover-photo {
    position: absolute;
    inset: 0;
    background:
      radial-gradient(ellipse 30% 45% at 48% 52%, rgba(235, 225, 215, 0.75) 0%, rgba(190, 160, 150, 0.45) 40%, rgba(0,0,0,0) 75%),
      radial-gradient(ellipse 48% 22% at 40% 86%, rgba(200, 195, 180, 0.45) 0%, rgba(0,0,0,0) 70%),
      radial-gradient(ellipse 60% 60% at 45% 45%, #2a1a26 0%, #0a060a 70%, #030103 100%);
  }
  .title {
    position: absolute;
    left: 30px;
    top: 48px;
    width: 830px;
    text-align: center;
    font-family: "Comfortaa", sans-serif;
    font-weight: 300;
    font-size: 168px;
    line-height: 1;
    letter-spacing: 8px;
    color: var(--glow);
    text-shadow: 0 0 6px var(--glow-halo), 0 0 16px var(--glow-halo), 0 0 28px rgba(190, 90, 230, 0.6);
  }
  .subtitle {
    position: absolute;
    left: 390px;
    top: 282px;
    font-family: "Cinzel", serif;
    font-size: 46px;
    letter-spacing: 20px;
    color: var(--plum);
  }
  .ghost-subtitle {
    position: absolute;
    left: -30px;
    top: 555px;
    font-family: "Cinzel", serif;
    font-size: 30px;
    letter-spacing: 22px;
    color: var(--ghost);
  }
  .authors {
    position: absolute;
    left: 0;
    top: 0;
    width: 100%;
    height: 100%;
    font-family: "Great Vibes", cursive;
    color: var(--plum);
    text-shadow: 1px 1px 0 var(--plum-deep), 0 0 2px #fff;
  }
  .author {
    position: absolute;
    font-size: 82px;
    line-height: 1;
    white-space: nowrap;
  }
  .author-first { left: 18px; top: 985px; }
  .author-second { left: 318px; top: 1070px; }
</style>
</head>
<body>
<main class="canvas">
  <div class="guide-line"></div>
  <section class="cover">
    <div class="cover-photo" role="img" aria-label="Photograph of a ballet dancer's legs en pointe in satin pointe shoes, lit from above against a dark stage with drifting chalk dust"></div>
    <h1 class="title">tamsire</h1>
    <p class="subtitle">A Memoir</p>
    <p class="ghost-subtitle" aria-hidden="true">Memoir A</p>
    <div class="authors">
      <p class="author author-first">Willa Hartley</p>
      <p class="author author-second">Nora Penwell</p>
    </div>
  </section>
</main>
</body>
</html>
```